BrivaTrek Freight Services Business cards

Would like a very unique design catchy but professional for business cards. Please use log provided.Marlon WellsCeo and Founder TransCon Logistix Solutions1-888-913-3225mwells@tlsolutionsus.comwww.bfservicesco.com

```html
<!DOCTYPE html>
<html lang="en">
<head>
<meta charset="utf-8">
<title>BrivaTrek Freight Services – Business Cards</title>
<link href="https://fonts.googleapis.com/css2?family=Roboto:wght@400;500;700&display=swap" rel="stylesheet">
<style>
  :root {
    --backdrop: #3a3a3a;
    --brand-blue: #1b7fca;
    --brand-blue-pattern: #2a8ad2;
    --card-white: #ffffff;
    --ink-grey: #555555;
    --icon-blue: #1b7fca;
  }
  * { margin: 0; padding: 0; box-sizing: border-box; }
  html, body {
    width: 1200px; height: 960px; overflow: hidden;
    background: var(--backdrop);
    font-family: "Roboto", sans-serif;
  }
  .card {
    position: absolute;
    left: 250px;
    width: 700px; height: 400px;
    box-shadow: 0 10px 30px rgba(0,0,0,.45);
    overflow: hidden;
  }
  /* Back side */
  .card-back { top: 50px; background: var(--brand-blue); }
  .card-back .pattern-fill {
    position: absolute; inset: 0;
    background: linear-gradient(135deg, var(--brand-blue-pattern), var(--brand-blue));
  }
  .card-back .brand-name {
    position: absolute; right: 70px; top: 168px;
    display: flex; align-items: center; gap: 12px;
    color: var(--card-white);
    font-weight: 700; font-size: 26px; letter-spacing: .5px;
  }
  .brand-mark-square {
    width: 26px; height: 26px; background: currentColor; display: inline-block;
  }
  /* Front side */
  .card-front { top: 500px; background: var(--card-white); }
  .name-band {
    position: absolute; left: 0; top: 110px;
    width: 390px; height: 90px;
    background: var(--brand-blue);
    color: var(--card-white);
    padding: 20px 0 0 50px;
  }
  .person-name { font-weight: 700; font-size: 28px; text-transform: uppercase; line-height: 1; }
  .person-title { font-weight: 400; font-size: 18px; text-transform: uppercase; margin-top: 6px; }
  .front-brand {
    position: absolute; left: 410px; top: 60px; width: 260px;
    display: flex; align-items: center; gap: 10px;
    color: var(--brand-blue);
    font-weight: 500; font-size: 22px; line-height: 1.15;
  }
  .front-brand .brand-mark-square { flex: none; width: 22px; height: 22px; }
  .website {
    position: absolute; right: 40px; top: 230px;
    color: var(--ink-grey); font-size: 17px;
  }
  .contact-list {
    position: absolute; left: 50px; bottom: 40px;
    list-style: none; color: var(--ink-grey); font-size: 18px;
  }
  .contact-list li { display: flex; align-items: center; gap: 12px; margin-top: 8px; }
  .contact-list svg { width: 18px; height: 18px; fill: var(--icon-blue); flex: none; }
</style>
</head>
<body>
  <section class="card card-back">
    <div class="pattern-fill" role="img" aria-label="Repeating tonal monogram pattern in light blue"></div>
    <div class="brand-name"><span class="brand-mark-square"></span>BrivaTrek Freight Services</div>
  </section>

  <section class="card card-front">
    <div class="name-band">
      <p class="person-name">Dustin Harrow</p>
      <p class="person-title">CEO &amp; Founder</p>
    </div>
    <div class="front-brand"><span class="brand-mark-square"></span>BrivaTrek Freight Services</div>
    <p class="website">www.bfservicesco.com</p>
    <ul class="contact-list">
      <li>
        <svg viewBox="0 0 24 24" aria-hidden="true"><path d="M6.6 10.8a15.1 15.1 0 0 0 6.6 6.6l2.2-2.2a1 1 0 0 1 1-.25 11.4 11.4 0 0 0 3.6.57 1 1 0 0 1 1 1V20a1 1 0 0 1-1 1A17 17 0 0 1 3 4a1 1 0 0 1 1-1h3.5a1 1 0 0 1 1 1c0 1.25.2 2.45.57 3.57a1 1 0 0 1-.25 1z"/></svg>
        <span>1-888-472-6081</span>
      </li>
      <li>
        <svg viewBox="0 0 24 24" aria-hidden="true"><path d="M2 5h20v14H2z M2 5l10 8 10-8" /></svg>
        <span>dharrow@bfservicesco.com</span>
      </li>
    </ul>
  </section>
</body>
</html>
```